Vitalquorra.com

I need a web design for a Online Wellness Center based in Chicago, IL and it's called "Vitalquorra" We provide Health risk assessment to individuals and interventions. Our portal has a Health Activity tracker where our members record health activities and aerobic miles and biometric data. Our Online wellness center tracks the participant's progress toward health goals and awards points for completed activities.
I started working on this website but the designer was not able to designer a website which describes what we do. I need a fresh look on this project. I need a very attractive, responsive website which says what we do.
These are the things we do.
1. We provide Health Risk Assessments to individuals and Co-operations
2. We Provide Free health screenings to undeserved communities
3. Assist individuals access free or affordable medications
4. We ask providers/doctors to see (or do a complete physical) one individual free of charge once a year (those individuals who are no insured and don't have money to pay from their pocket)
5. Assist patient access lab work at low cost
Our goal is to provide services that will lower the cost of care for our members.

Here is the website: www.vitalquorra.com still underdevelopment. PLEASE DO NOT COPY THIS STYLE OF WEBSITE. IT'S A BAD DESIGN AND THAT IS WHY I'M RE-DESIGNING THE SITE

Target Market(s)

Health individuals between the age of 21 to 65 Plus years old. Insured and uninsured

Industry/Entity Type

Health And Wellness

Coding

Coded - Design and coding required

Number of Pages Required

5+ page

Colors
0292cd

Requirements
Must have
• I'm still working on this websiteHere is the menu: Home, About us, Services, Health Screening, Providers, Contacts
• Please see. www.vitalquorra.com
Nice to have
• Event calender
• Upcoming Event
• Medication
• Lab assist
• Providers/Free Clinics

```html
<!DOCTYPE html>
<html lang="en">
<head>
<meta charset="utf-8">
<title>Vitalquorra – Online Wellness Center</title>
<link href="https://fonts.googleapis.com/css2?family=Open+Sans:wght@400;600;700&display=swap" rel="stylesheet">
<style>
:root{
  --blue:#0292cd;
  --blue-dark:#0278ad;
  --blue-deep:#026a99;
  --ink:#333a40;
  --muted:#7a8288;
  --line:#d9dde0;
  --band:#eef0f2;
  --white:#ffffff;
  --accent-red:#d9534f;
}
*{box-sizing:border-box;margin:0;padding:0}
html,body{width:1200px;height:2748px;overflow:hidden}
body{font-family:"Open Sans",Arial,sans-serif;color:var(--ink);background:var(--white);position:relative;font-size:13px}
.abs{position:absolute}
.btn{display:inline-block;background:var(--blue);color:var(--white);font-size:11px;font-weight:600;padding:7px 16px;border-radius:2px}

/* header */
.site-header{left:0;top:0;width:1200px;height:100px;background:var(--white)}
.brand{left:180px;top:22px;display:flex;align-items:center;gap:10px}
.brand-mark{width:30px;height:30px;border-radius:50%;background:var(--blue)}
.brand-name{font-size:26px;font-weight:700;color:var(--blue)}
.brand-tag{left:220px;top:56px;font-size:10px;color:var(--muted)}
.account{right:180px;top:14px;font-size:10px;color:var(--muted);display:flex;gap:16px}
.account span::before{content:"";display:inline-block;width:7px;height:7px;background:var(--muted);border-radius:50%;margin-right:5px}
.main-nav{right:180px;top:62px;display:flex}
.main-nav a{font-size:12px;color:var(--ink);padding:9px 13px;text-decoration:none}
.main-nav a.active{background:var(--blue);color:var(--white)}

/* hero */
.hero{left:0;top:100px;width:1200px;height:560px;background:linear-gradient(100deg,#d8dde2 0%,#b9c6cf 35%,#d9c8b6 65%,#ece6de 100%)}
.hero-links{left:180px;top:114px;font-size:10px;color:var(--blue-deep)}
.hero-caption{left:200px;top:430px;width:540px;height:150px;background:rgba(30,40,50,.72);padding:18px 22px;color:var(--white)}
.hero-caption h1{font-size:24px;font-weight:600;margin-bottom:8px}
.hero-caption p{font-size:11px;line-height:1.55;color:#e4e8eb}
.hero-caption .more{position:absolute;right:22px;bottom:12px;font-size:11px}

/* feature cards */
.feature{top:690px;width:410px;height:260px;display:flex}
.feature-photo{width:50%;height:100%;background:linear-gradient(160deg,#cfd8de,#9fb4c2)}
.feature-text{width:50%;height:100%;background:var(--blue);color:var(--white);padding:22px 18px}
.feature-text h3{font-size:16px;font-weight:600;margin-bottom:10px}
.feature-text p{font-size:11px;line-height:1.55;margin-bottom:16px}
.feature-text .btn{background:var(--white);color:var(--blue)}

/* services */
.service{top:990px;width:240px;text-align:center}
.service-icon{width:72px;height:72px;margin:0 auto 14px;display:block}
.service h3{font-size:16px;color:var(--blue);font-weight:600;margin-bottom:10px}
.service p{font-size:11px;line-height:1.6;color:var(--muted);margin-bottom:26px}

/* appointment */
.appointment{left:0;top:1350px;width:1200px;height:330px;background:var(--band)}
.doctor-photo{left:160px;top:1340px;width:290px;height:340px;background:linear-gradient(180deg,#e9eef2,#c9d6df)}
.appointment h2{left:460px;top:1388px;width:560px;text-align:center;font-size:26px;font-weight:600}
.form{left:460px;top:1450px;width:560px}
.row{display:flex;gap:16px;margin-bottom:12px}
.field{flex:1;height:30px;background:var(--white);border:1px solid var(--line);font-size:11px;color:var(--muted);padding:7px 10px}
.field.tall{height:40px}
.submit{left:692px;top:1578px;width:100px;text-align:center;padding:9px 0}

/* calendar + events */
.section-title{font-size:18px;font-weight:600;padding-bottom:8px;border-bottom:2px solid var(--line);position:relative}
.section-title::after{content:"";position:absolute;left:0;bottom:-2px;width:60px;height:2px;background:var(--blue)}
.calendar{left:180px;top:1700px;width:380px}
.cal-head{margin-top:16px;background:var(--blue);color:var(--white);font-weight:600;font-size:14px;display:flex;justify-content:space-between;padding:8px 14px}
.cal{width:100%;border-collapse:collapse;font-size:11px;text-align:center}
.cal th{background:#e4e8eb;padding:5px 0;font-weight:600}
.cal td{border:1px solid var(--line);padding:6px 0;background:#f7f8f9}
.cal td.off{color:#b4babf}
.cal td.today{background:var(--accent-red);color:var(--white)}
.upcoming{left:600px;top:1700px;width:420px}
.event{display:flex;gap:14px;margin-top:16px;position:relative;padding-bottom:26px}
.event-date{width:34px;flex:none;text-align:center;font-size:9px;color:var(--muted)}
.event p{font-size:11px;line-height:1.55;color:var(--muted)}
.event .btn{position:absolute;right:0;bottom:0;padding:4px 10px;font-size:10px}

/* recent events */
.recent{left:180px;top:2070px;width:840px}
.recent-card{top:2130px;width:260px;height:310px;background:#f3f4f5;border:1px solid var(--line)}
.recent-card .plus{position:absolute;right:0;top:0;width:60px;height:60px;background:#c9ced2}
.recent-date{position:absolute;left:0;top:60px;width:200px;text-align:center}
.recent-date .m{font-size:14px;font-weight:600;letter-spacing:1px}
.recent-date .d{font-size:46px;font-weight:700;line-height:1.2}
.recent-date .w{font-size:14px;font-weight:600}
.recent-card .bar{position:absolute;left:0;bottom:0;width:100%;height:50px;background:var(--blue);color:var(--white);font-size:12px;display:flex;align-items:center;justify-content:center;gap:8px}

/* footer */
.site-footer{left:0;top:2488px;width:1200px;height:260px;background:var(--blue);color:var(--white)}
.tweet{left:180px;top:2508px;width:840px;display:flex;gap:20px;align-items:flex-start}
.tweet-dot{width:36px;height:36px;border-radius:50%;background:var(--white);flex:none}
.tweet p{font-size:12px;line-height:1.6}
.foot-col{top:2590px;width:250px;font-size:10px;line-height:1.7}
.foot-col h4{font-size:12px;font-weight:600;margin-bottom:6px}
.foot-col li{list-style:none;border-bottom:1px solid rgba(255,255,255,.25);padding:2px 0}
.copyright{left:0;top:2722px;width:1200px;height:26px;background:var(--blue-deep);font-size:10px;text-align:center;line-height:26px}
</style>
</head>
<body>

<header class="abs site-header">
  <div class="abs brand"><span class="brand-mark"></span><span class="brand-name">Vitalquorra</span></div>
  <div class="abs brand-tag">Your online wellness center</div>
  <div class="abs account"><span>Login</span><span>Sign Up</span></div>
  <nav class="abs main-nav">
    <a class="active">Home</a><a>About us</a><a>Services</a><a>Health Screening</a><a>Providers</a><a>Contact</a>
  </nav>
</header>

<div class="abs hero" role="img" aria-label="Photo of a doctor and a patient reviewing results together"></div>
<div class="abs hero-links">Call Us Today | Contact Us</div>
<div class="abs hero-caption">
  <h1>Lorem Ipsum is simply dummy text ?</h1>
  <p>Lorem Ipsum is simply dummy text of the printing and typesetting industry. Lorem Ipsum has been the industry's standard dummy text ever since the 1500s, when an unknown printer took a galley of type and scrambled it to make a type specimen book.</p>
  <span class="more">» Read More</span>
</div>

<section class="abs feature" style="left:180px">
  <div class="feature-photo" role="img" aria-label="Photo of a nurse assisting a patient"></div>
  <div class="feature-text"><h3>Lorem Ipsum</h3><p>Lorem Ipsum is simply dummy text of the printing and typesetting industry standard.</p><span class="btn">Read More</span></div>
</section>
<section class="abs feature" style="left:610px">
  <div class="feature-text"><h3>Lorem Ipsum</h3><p>Lorem Ipsum is simply dummy text of the printing and typesetting industry standard.</p><span class="btn">Read More</span></div>
  <div class="feature-photo" role="img" aria-label="Photo of a smiling woman during a health screening"></div>
</section>

<div class="abs service" style="left:180px">
  <svg class="service-icon" viewBox="0 0 72 72"><circle cx="36" cy="36" r="33" fill="none" stroke="#0292cd" stroke-width="3"/><path d="M36 50 L22 36 a8 8 0 0 1 14 -10 a8 8 0 0 1 14 10 Z" fill="none" stroke="#0292cd" stroke-width="3"/></svg>
  <h3>Lorem Ipsum</h3><p>Lorem Ipsum is simply dummy text of the printing and typesetting industry. Lorem Ipsum has been the industry's standard dummy text.</p><span class="btn">Read More</span>
</div>
<div class="abs service" style="left:480px">
  <svg class="service-icon" viewBox="0 0 72 72"><circle cx="36" cy="36" r="33" fill="none" stroke="#0292cd" stroke-width="3"/><path d="M26 20 v14 a10 10 0 0 0 20 0 v-14 M36 44 v6 a6 6 0 0 0 12 0 v-4" fill="none" stroke="#0292cd" stroke-width="3"/><circle cx="48" cy="43" r="3" fill="#0292cd"/></svg>
  <h3>Lorem Ipsum</h3><p>Lorem Ipsum is simply dummy text of the printing and typesetting industry. Lorem Ipsum has been the industry's standard dummy text.</p><span class="btn">Read More</span>
</div>
<div class="abs service" style="left:780px">
  <svg class="service-icon" viewBox="0 0 72 72"><circle cx="36" cy="36" r="33" fill="none" stroke="#0292cd" stroke-width="3"/><path d="M36 52 L20 36 a9 9 0 0 1 16 -11 a9 9 0 0 1 16 11 Z" fill="none" stroke="#0292cd" stroke-width="3"/><path d="M24 37 h7 l3 -6 l4 10 l3 -4 h7" fill="none" stroke="#0292cd" stroke-width="2.5"/></svg>
  <h3>Lorem Ipsum</h3><p>Lorem Ipsum is simply dummy text of the printing and typesetting industry. Lorem Ipsum has been the industry's standard dummy text.</p><span class="btn">Read More</span>
</div>

<section class="abs appointment"></section>
<div class="abs doctor-photo" role="img" aria-label="Photo of a doctor in a white coat with a stethoscope"></div>
<h2 class="abs" style="left:460px;top:1388px;width:560px;text-align:center;font-size:26px;font-weight:600">Fix An Appointment</h2>
<form class="abs form">
  <div class="row"><div class="field">Name</div><div class="field">Phone</div></div>
  <div class="row"><div class="field">Email</div><div class="field">Date - mm/dd/yyyy</div></div>
  <div class="row"><div class="field tall">Message</div></div>
</form>
<span class="abs btn submit">Submit</span>

<section class="abs calendar">
  <h2 class="section-title">Calendar</h2>
  <div class="cal-head"><span>‹</span><span>July 2011</span><span>›</span></div>
  <table class="cal">
    <tr><th>Su</th><th>Mo</th><th>Tu</th><th>We</th><th>Th</th><th>Fr</th><th>Sa</th></tr>
    <tr><td class="off">26</td><td class="off">27</td><td class="off">28</td><td class="off">29</td><td class="off">30</td><td>1</td><td>2</td></tr>
    <tr><td>3</td><td>4</td><td>5</td><td>6</td><td>7</td><td>8</td><td>9</td></tr>
    <tr><td>10</td><td>11</td><td>12</td><td>13</td><td>14</td><td>15</td><td>16</td></tr>
    <tr><td>17</td><td class="today">18</td><td>19</td><td>20</td><td>21</td><td>22</td><td>23</td></tr>
    <tr><td>24</td><td>25</td><td>26</td><td>27</td><td>28</td><td>29</td><td>30</td></tr>
    <tr><td>31</td><td class="off">1</td><td class="off">2</td><td class="off">3</td><td class="off">4</td><td class="off">5</td><td class="off">6</td></tr>
  </table>
</section>

<section class="abs upcoming">
  <h2 class="section-title">Upcoming Events</h2>
  <div class="event">
    <div class="event-date"><svg width="30" height="30" viewBox="0 0 30 30"><rect x="2" y="5" width="26" height="23" fill="none" stroke="#0292cd" stroke-width="2"/><rect x="2" y="5" width="26" height="7" fill="#0292cd"/></svg><br>18 Sept</div>
    <p>Lorem Ipsum is simply dummy text of the printing and typesetting industry. Lorem Ipsum has been the industry's standard dummy text of typesetting ever since the 1500s.</p>
    <span class="btn">Read More</span>
  </div>
  <div class="event">
    <div class="event-date"><svg width="30" height="30" viewBox="0 0 30 30"><rect x="2" y="5" width="26" height="23" fill="none" stroke="#0292cd" stroke-width="2"/><rect x="2" y="5" width="26" height="7" fill="#0292cd"/></svg><br>11 Sept</div>
    <p>Lorem Ipsum is simply dummy text of the printing and typesetting industry. Lorem Ipsum has been the industry's standard dummy text of typesetting ever since the 1500s.</p>
    <span class="btn">Read More</span>
  </div>
</section>

<h2 class="abs recent section-title">Recent Events</h2>
<div class="abs recent-card" style="left:180px"><span class="plus"></span><div class="recent-date"><div class="m">SEPTEMBER</div><div class="d">18</div><div class="w">FRIDAY</div></div><div class="bar"><svg width="12" height="16" viewBox="0 0 12 16"><path d="M6 0a6 6 0 0 1 6 6c0 4-6 10-6 10S0 10 0 6a6 6 0 0 1 6-6z" fill="#fff"/><circle cx="6" cy="6" r="2" fill="#0292cd"/></svg>Lorem Ipsum is simply</div></div>
<div class="abs recent-card" style="left:470px"><span class="plus"></span><div class="recent-date"><div class="m">SEPTEMBER</div><div class="d">11</div><div class="w">FRIDAY</div></div><div class="bar"><svg width="12" height="16" viewBox="0 0 12 16"><path d="M6 0a6 6 0 0 1 6 6c0 4-6 10-6 10S0 10 0 6a6 6 0 0 1 6-6z" fill="#fff"/><circle cx="6" cy="6" r="2" fill="#0292cd"/></svg>Lorem Ipsum is simply</div></div>
<div class="abs recent-card" style="left:760px"><span class="plus"></span><div class="recent-date"><div class="m">SEPTEMBER</div><div class="d">08</div><div class="w">TUESDAY</div></div><div class="bar"><svg width="12" height="16" viewBox="0 0 12 16"><path d="M6 0a6 6 0 0 1 6 6c0 4-6 10-6 10S0 10 0 6a6 6 0 0 1 6-6z" fill="#fff"/><circle cx="6" cy="6" r="2" fill="#0292cd"/></svg>Lorem Ipsum is simply</div></div>

<footer class="abs site-footer"></footer>
<div class="abs tweet"><span class="tweet-dot"></span><p>Lorem Ipsum is simply dummy text of the printing and typesetting industry. Lorem Ipsum has been the industry's standard dummy text ever since the 1500s.</p></div>
<div class="abs foot-col" style="left:180px"><h4>About us</h4><p>Vitalquorra is an online wellness center helping members track health activities, complete assessments and earn points toward their personal goals.</p><p>» Read More</p></div>
<div class="abs foot-col" style="left:475px"><h4>Why Us</h4><ul><li>Free health risk assessments</li><li>Free community health screenings</li><li>Affordable medication assistance</li><li>Low cost lab work access</li></ul></div>
<div class="abs foot-col" style="left:770px"><h4>Get In Touch</h4><p>+1 (312) 555-0148<br>info@vitalquorra.com<br>www.vitalquorra.com<br>240 Lakeview Avenue<br>Chicago, IL 60601</p></div>
<div class="abs copyright">Copyright © 2011 Vitalquorra. All rights reserved.</div>

</body>
</html>
```